Electronic Refurbishment Warehouse needs a Website

We are looking for a clean, professional looking design with iconic imagery. Our main point we want to get across is that we will help clients save time, and money, and provide outstanding quality. Our logo can be found in the uploads section. This site is used to impress clients that we have a pre-existing relationship with. This site will be available for the public but it will not be used to advertise to the public or to drive traffic to it. The color scheme we are looking to stay with is blue, but that is not to say that everything should be a shade of blue. Last note, see site map below.

Site Map:

Home
Company
a. company overview
b. CEO letter
Services
a. Remanufacture & Refurbishment Services
1. Consumer Electronics
2. Cellular Phones
b.Reverse Logistics Management
c.Warranty Repair & Field Services
d.Quality Control & Assurance
e.Warehousing & Distribution
Careers
Contact Us

Reason: We want to allocate more time for designers to do what they do best.

Target Market(s)

Phone and TV Retailers that may have units that need to be refurbished. Example Velorin, tallcart, qvo, etc.

Industry/Entity Type

Electronics

Requirements
Must have
• Home Page Slider.
Iconic imagery and navigation.
The ability to be put into the 960 Grid.

```html
<!DOCTYPE html>
<html lang="en">
<head>
<meta charset="utf-8">
<title>Norvale Group — Return, Refurbish, Repair</title>
<link href="https://fonts.googleapis.com/css2?family=Arimo:wght@400;700&family=Source+Sans+3:wght@400;600;700&display=swap" rel="stylesheet">
<style>
:root{
  --brand-blue:#2f7cc0;
  --hero-blue:#9ecadb;
  --hero-ink:#3e6b7f;
  --ink:#444;
  --muted:#8a8a8a;
  --link:#2f7cc0;
  --strip:#e6e6e6;
  --footer:#6a8596;
  --footer-bar:#5a7283;
  --footer-text:#eef3f6;
  --white:#fff;
}
*{box-sizing:border-box;margin:0;padding:0}
html,body{width:1200px;height:1041px;overflow:hidden;background:var(--white)}
.page{width:1308px;height:1135px;transform:scale(0.9174);transform-origin:0 0;position:relative;font-family:"Arimo",Arial,sans-serif;color:var(--ink)}
/* header */
.site-header{position:absolute;left:0;top:0;width:1308px;height:105px;background:linear-gradient(#fff,#f3f3f3);border-bottom:1px solid #ddd;box-shadow:0 2px 4px rgba(0,0,0,.08)}
.brand{position:absolute;left:158px;top:32px;display:flex;align-items:center;gap:12px;font-family:"Source Sans 3",sans-serif;font-weight:700;font-size:30px;color:var(--brand-blue);white-space:nowrap}
.brand-mark{width:44px;height:44px;background:var(--brand-blue)}
.contact-bar{position:absolute;top:12px;font-size:11px;color:#555;display:flex;align-items:center;gap:6px;white-space:nowrap}
.contact-bar svg{display:block}
.contact-bar.email span{text-decoration:underline;color:#333}
.login{position:absolute;left:1019px;top:0;width:134px;height:33px;background:#e9e9e9;color:#777;font-size:11px;display:flex;align-items:center;justify-content:center}
.main-nav{position:absolute;top:74px;left:0;font-family:"Source Sans 3",sans-serif;font-size:15px;font-weight:600;color:var(--muted);text-transform:uppercase}
.main-nav a{position:absolute;white-space:nowrap;display:flex;align-items:center;gap:5px;color:inherit;text-decoration:none}
.main-nav a.current{color:#222;font-weight:700}
.nav-caret{position:absolute;left:560px;top:93px;width:0;height:0;border:6px solid transparent;border-bottom-color:var(--hero-blue)}
/* hero */
.hero{position:absolute;left:0;top:105px;width:1308px;height:320px;background:linear-gradient(var(--hero-blue),#a6d0df)}
.hero-title{position:absolute;left:222px;top:62px;font-family:"Source Sans 3",sans-serif;font-weight:600;font-size:47px;color:#fff;line-height:1}
.hero-sub{position:absolute;left:221px;top:115px;font-family:"Source Sans 3",sans-serif;font-weight:600;font-size:27px;color:var(--hero-ink);line-height:34px;white-space:nowrap}
.btn{position:absolute;background:linear-gradient(#fff,#ececec);border:1px solid #c9c9c9;border-radius:3px;font-family:"Source Sans 3",sans-serif;color:#555;display:flex;align-items:center;justify-content:center;white-space:nowrap}
.hero .btn{left:221px;top:205px;width:129px;height:30px;font-size:16px}
.slider-arrow{position:absolute;top:112px;width:48px;height:48px;border-radius:50%;background:rgba(255,255,255,.35);display:flex;align-items:center;justify-content:center}
.devices{position:absolute;left:703px;top:42px;width:387px;height:238px;background:linear-gradient(90deg,#2b2b2b,#3a3a3a 40%,#ddd 41%,#2a2a2a 42%,#3a3a3a 70%,#888 72%,#666);border-radius:8px;opacity:.9}
/* services strip */
.services-strip{position:absolute;left:0;top:425px;width:1308px;height:124px;background:var(--strip);border-top:1px solid #d2d2d2;border-bottom:1px solid #d2d2d2}
.service{position:absolute;top:0;height:124px;display:flex;align-items:center;gap:14px;font-family:"Source Sans 3",sans-serif;font-size:14.5px;line-height:17px;color:#222;white-space:nowrap}
.service-icon{width:54px;height:54px;border-radius:6px;flex:none}
.divider{position:absolute;top:12px;height:96px;border-left:1px dotted #bbb}
/* content */
.panel{position:absolute;top:549px;height:275px;border-left:1px solid #ddd;border-right:1px solid #ddd;background:linear-gradient(#f7f7f7,#fff 60px)}
.panel h2{position:absolute;font-family:"Source Sans 3",sans-serif;font-weight:400;color:#444;white-space:nowrap}
.panel p{position:absolute;font-size:12.5px;line-height:18px;color:var(--ink)}
.welcome h2{left:54px;top:28px;font-size:25px}
.welcome h2 b{color:var(--brand-blue);font-weight:600}
.welcome h2 strong{color:#444;font-weight:600}
.title-mark{position:absolute;left:20px;top:36px;width:22px;height:22px;background:var(--brand-blue)}
.news h2{left:28px;top:28px;font-size:25px}
.news-date{position:absolute;font-size:11px;color:var(--link)}
.news-more{position:absolute;font-size:11px;color:var(--link)}
.news-sep{position:absolute;left:28px;width:282px;border-top:1px dotted #ccc}
/* footer */
.site-footer{position:absolute;left:0;top:868px;width:1308px;height:267px;background:var(--footer);border-top:1px solid #5c7687}
.footer-col{position:absolute;top:40px}
.footer-col h3{font-weight:400;font-size:12px;color:var(--footer-text);text-transform:uppercase;padding-bottom:6px;border-bottom:1px solid #8aa0ae}
.footer-col ul{list-style:none;margin-top:8px}
.footer-col li{font-size:11px;color:var(--footer-text);line-height:18px;padding-left:1px;white-space:nowrap}
.footer-col li.sub{padding-left:13px}
.social li{display:flex;align-items:center;gap:6px;line-height:30px}
.social .sq{width:15px;height:15px;background:#4a7fae;border-radius:2px}
.footer-bar{position:absolute;left:207px;top:212px;width:888px;height:43px;background:var(--footer-bar);border-radius:2px;font-size:11px;color:#c8d4dc;display:flex;align-items:center;justify-content:center}
</style>
</head>
<body>
<div class="page">
  <header class="site-header">
    <div class="brand"><span class="brand-mark"></span>Norvale group</div>
    <div class="contact-bar" style="left:700px">
      <svg width="20" height="14" viewBox="0 0 20 14"><path d="M2 5c4-4 12-4 16 0l-2 2-3-1V4H7v2L4 7z" fill="#6a9ccc"/><rect x="4" y="8" width="12" height="5" rx="1" fill="#6a9ccc"/></svg>
      <span>(1-800) 555-0147</span>
    </div>
    <div class="contact-bar email" style="left:845px">
      <svg width="22" height="14" viewBox="0 0 22 14"><rect x="1" y="1" width="20" height="12" fill="#6a9ccc"/><path d="M1 1l10 7 10-7" stroke="#fff" fill="none"/></svg>
      <span>information@norvale.com</span>
    </div>
    <div class="login">Employee Login</div>
    <nav class="main-nav">
      <a class="current" style="left:530px"><svg width="13" height="12" viewBox="0 0 13 12"><path d="M6.5 0L0 6h2v6h3V8h3v4h3V6h2z" fill="#222"/></svg>Home</a>
      <a style="left:646px"><svg width="11" height="12" viewBox="0 0 11 12"><circle cx="5.5" cy="3" r="3" fill="#aaa"/><path d="M0 12c0-4 2-5 5.5-5S11 8 11 12z" fill="#aaa"/></svg>Company</a>
      <a style="left:793px"><svg width="12" height="12" viewBox="0 0 12 12"><circle cx="6" cy="6" r="5.5" fill="#aaa"/></svg>Services</a>
      <a style="left:930px"><svg width="12" height="13" viewBox="0 0 12 13"><rect x="0.5" y="0.5" width="11" height="12" fill="none" stroke="#aaa"/><path d="M3 4h6M3 7h6M3 10h4" stroke="#aaa"/></svg>Careers</a>
      <a style="left:1068px"><svg width="12" height="12" viewBox="0 0 12 12"><path d="M2 1c-2 3 0 8 4 10l2-2-2-2-1 1c-1-1-2-2-2-4l1-1-2-2z" fill="#aaa"/></svg>Contact</a>
    </nav>
  </header>
  <div class="nav-caret"></div>

  <section class="hero">
    <div class="slider-arrow" style="left:154px"><svg width="12" height="14" viewBox="0 0 12 14"><path d="M9 1L3 7l6 6" stroke="#fff" stroke-width="3" fill="none"/></svg></div>
    <h1 class="hero-title">We are the</h1>
    <p class="hero-sub">Return / Refurbish / Repair Specialists<br>behind the brand.</p>
    <a class="btn">Read More</a>
    <div class="devices" role="img" aria-label="A tablet and two smartphones standing side by side"></div>
    <div class="slider-arrow" style="left:1101px"><svg width="12" height="14" viewBox="0 0 12 14"><path d="M3 1l6 6-6 6" stroke="#fff" stroke-width="3" fill="none"/></svg></div>
  </section>

  <section class="services-strip">
    <div class="service" style="left:155px"><div class="service-icon" role="img" aria-label="Crossed screwdriver and wrench" style="background:linear-gradient(135deg,#d33 0,#99a 50%,#3a6fc9)"></div>Remanufacture and<br>Refurbishment<br>Services</div>
    <div class="divider" style="left:353px"></div>
    <div class="service" style="left:370px"><div class="service-icon" role="img" aria-label="Toolbox with tools" style="background:linear-gradient(135deg,#c33,#bbb 60%,#37c)"></div>Factory Repair<br>Services</div>
    <div class="divider" style="left:545px"></div>
    <div class="service" style="left:566px"><div class="service-icon" role="img" aria-label="Document with a gear" style="background:linear-gradient(135deg,#f4f4f4,#9aa4ab)"></div>Reverse Logistics<br>Management</div>
    <div class="divider" style="left:755px"></div>
    <div class="service" style="left:772px"><svg class="service-icon" viewBox="0 0 54 54" aria-label="Check mark" role="img"><rect x="2" y="6" width="48" height="4" fill="#8cc63f"/><path d="M4 30l14 14L50 12" stroke="#3a8fd0" stroke-width="9" fill="none"/></svg>Quality Control and<br>Assurance Services</div>
    <div class="divider" style="left:963px"></div>
    <div class="service" style="left:978px"><div class="service-icon" role="img" aria-label="Warehouse building" style="background:linear-gradient(135deg,#b07050,#6b3a22)"></div>Warehousing and<br>Distribution</div>
  </section>

  <section class="panel welcome" style="left:155px;width:661px">
    <span class="title-mark"></span>
    <h2>Welcome to <b>Norvale</b> <strong>Group</strong></h2>
    <p style="left:19px;top:74px;width:590px">Over the past 20 years, we have dedicated ourselves to building strong relationships with our clients, providing them with cost-saving, flexible solutions to meet their reverse logistics needs.</p>
    <p style="left:19px;top:128px;width:590px">Norvale offers services that allow you to effectively manage your company’s product returns.&nbsp; Our clients look to us for all their reverse logistics needs.&nbsp; Let us help you devise solutions to maximize your company’s success.</p>
    <a class="btn" style="left:17px;top:210px;width:98px;height:24px;font-size:12px">Read More</a>
  </section>

  <section class="panel news" style="left:815px;width:339px;border-left:none">
    <h2>News &amp; Updates</h2>
    <p style="left:29px;top:74px;width:285px">Norvale, a large reverse logistics services provider, is pleased to announce...</p>
    <span class="news-date" style="left:30px;top:116px">15.Feb.2012</span>
    <span class="news-more" style="left:246px;top:116px">Read More »</span>
    <div class="news-sep" style="top:151px"></div>
    <p style="left:29px;top:171px;width:285px">As more and more companies recognize their corporate responsibility...</p>
    <span class="news-date" style="left:30px;top:213px">15.Feb.2012</span>
    <span class="news-more" style="left:246px;top:213px">Read More »</span>
  </section>

  <footer class="site-footer">
    <div class="footer-col" style="left:205px;width:158px">
      <h3>Company</h3>
      <ul><li>Company overview</li><li>CEO letter</li></ul>
    </div>
    <div class="footer-col" style="left:376px;width:248px">
      <h3>Services</h3>
      <ul>
        <li>Remanufacture &amp; Refurbishment Services</li>
        <li class="sub">Consumer Electronics</li>
        <li class="sub">Cellular Phones</li>
        <li>Reverse Logistics Management</li>
        <li>Warranty Repair &amp; Field Services</li>
        <li>Quality Control &amp; Assurance</li>
        <li>Warehousing &amp; Distribution</li>
      </ul>
    </div>
    <div class="footer-col" style="left:637px;width:126px">
      <h3>Other</h3>
      <ul><li>Careers</li><li>News</li><li>Testimonials</li><li>Contact Us</li><li>Sitemap</li></ul>
    </div>
    <div class="footer-col social" style="left:775px;width:74px">
      <h3>Social</h3>
      <ul><li><span class="sq"></span>Friendwall</li><li><span class="sq" style="background:#5aa9d8"></span>Chirper</li><li><span class="sq" style="background:#2f6b9a"></span>LinkRoll</li></ul>
    </div>
    <div class="footer-bar">Norvale Group, Inc. © 2012,&nbsp; All rights reserved | Terms | Privacy Policy</div>
  </footer>
</div>
</body>
</html>
```